Web Design Project (uncoded)

About Us
ZipRoam is a telecom startup and is looking to launch its website.
ZipRoam specializes in providing communication solutions to the travel market. Our mission is to develop cost effective communication products and solutions for the international traveler.
Our simple vision of "every hotel should have a mobile phone in the guest rooms", led us to develop a pathbreaking & cost effective mobile phone. With full integration capabilities with the hotels property management system, location based marketing, user locator and other features, this product is unique in addressing the hospitality segment.
The website is targeted at hotel owners and property management companies.
The website should have a young contemporary and a funky look, in line with the name.
Please find attached our logo (for the colors etc.). (attached now).
We would like to receive the design for a home page and an inside page for the website.
Site map would be as follows: Home, About Us, Solutions, Contact us
Thanks and look forward,
Tomas
Target Market(s)
Hotel decision makers
Industry/Entity Type
Property Management
Look and feel
Each slider illustrates characteristics of the customer's brand and the style your logo design should communicate.

```html
<!DOCTYPE html>
<html lang="en">
<head>
<meta charset="utf-8">
<title>ZipRoam – Home</title>
<link href="https://fonts.googleapis.com/css2?family=Questrial&family=Arimo:wght@400;700&display=swap" rel="stylesheet">
<style>
  :root {
    --orange: #f39a12;
    --orange-deep: #ee7d0c;
    --orange-band: #f2ac14;
    --page-bg: #f6f6f6;
    --heading: #626262;
    --body-text: #9a9a9a;
    --dots: #c9c9c9;
    --footer-bg: #1e1e1e;
    --footer-text: #e2e2e2;
    --box-border: #dcdcdc;
  }
  * { margin: 0; padding: 0; box-sizing: border-box; }
  html, body { width: 1200px; height: 900px; overflow: hidden; }
  body { position: relative; background: var(--page-bg); font-family: "Arimo", Arial, sans-serif; }
  .abs { position: absolute; }

  /* Hero */
  .hero-band { left: 0; top: 0; width: 1200px; height: 207px;
    background: linear-gradient(180deg, #f6b81c 0%, var(--orange-band) 100%); }
  .hero-shadow { left: 140px; top: 170px; width: 920px; height: 28px; border-radius: 50%;
    background: radial-gradient(ellipse at center, rgba(90,50,0,.45) 0%, rgba(90,50,0,0) 70%); }
  .hero-photo-left { left: 110px; top: 0; width: 484px; height: 178px;
    background: linear-gradient(120deg, #e7a04c 0%, #c97a3a 45%, #f2d2a6 100%); }
  .hero-photo-right { left: 600px; top: 0; width: 490px; height: 178px;
    background: linear-gradient(120deg, #cfc6bc 0%, #e9e6e2 50%, #b49a86 100%); }
  .hero-divider { left: 594px; top: 0; width: 6px; height: 178px; background: #f8c070; }
  .hero-caption-bar { left: 110px; top: 99px; width: 980px; height: 79px; background: rgba(255,255,255,.72); }
  .hero-caption { left: 155px; top: 125px; font-family: "Questrial", sans-serif; font-size: 21px;
    color: #2e2e2e; letter-spacing: .1px; }
  .hero-badge { left: 540px; top: -44px; width: 112px; height: 108px; }
  .hero-button { left: 858px; top: 114px; width: 172px; height: 52px; }
  .hero-button-label { left: 893px; top: 128px; font-family: "Questrial", sans-serif; font-size: 19px;
    font-weight: bold; color: #4a2a00; }

  /* Section headings */
  .section-icon { border-radius: 6px; }
  .icon-notepad { left: 120px; top: 226px; width: 66px; height: 58px;
    background: linear-gradient(135deg, #f4f1ea 0%, #c9c2b4 100%); }
  .icon-wallet { left: 116px; top: 479px; width: 64px; height: 60px;
    background: linear-gradient(135deg, #a46a30 0%, #6e4119 100%); }
  .section-title { font-family: "Questrial", sans-serif; font-weight: bold; font-size: 21px; color: var(--heading); }
  .dotted-rule { height: 0; border-top: 3px dotted var(--dots); }

  /* Why choose list */
  .reasons { left: 140px; top: 299px; list-style: none; }
  .reasons li { height: 30px; font-size: 13px; color: var(--body-text); display: flex; align-items: flex-start; }
  .reasons svg { width: 16px; height: 16px; margin-right: 10px; flex: none; }

  .about-text { left: 127px; top: 543px; width: 670px; font-size: 13px; line-height: 20px; color: var(--body-text); }
  .read-more-link { left: 738px; top: 661px; font-size: 12px; color: #555; text-decoration: underline; }

  /* Testimonial */
  .quote-box { left: 821px; top: 241px; width: 250px; height: 230px; border: 1px solid var(--box-border);
    background: linear-gradient(180deg, #f7f7f7 0%, #f7f7f7 55%, #e9e9e9 100%); }
  .quote-tail { left: 988px; top: 469px; width: 40px; height: 22px; }
  .quote-title { left: 851px; top: 253px; font-family: "Questrial", sans-serif; font-weight: bold; font-size: 18px; color: var(--orange-deep); }
  .quote-text { left: 852px; top: 292px; width: 205px; font-size: 12px; line-height: 20px; color: var(--body-text); }
  .client-photo { left: 824px; top: 480px; width: 59px; height: 59px; border: 3px solid #e2e2e2;
    background: linear-gradient(160deg, #7a4a33 0%, #b98568 100%); }
  .client-name { left: 896px; top: 495px; font-size: 12px; font-weight: bold; color: #555; }
  .client-role { left: 896px; top: 513px; font-size: 12px; font-weight: bold; color: #999; }

  /* Newsletter */
  .newsletter-title { left: 830px; top: 593px; font-size: 13px; font-weight: bold; color: #555; }
  .newsletter-input { left: 828px; top: 621px; width: 150px; height: 32px; border: 1px solid #d8d8d8;
    background: #fff; font-size: 12px; color: #999; padding: 8px 0 0 18px; border-radius: 3px 0 0 3px; }
  .newsletter-button { left: 977px; top: 621px; width: 109px; height: 32px; border-radius: 0 3px 3px 0;
    background: linear-gradient(180deg, #fba628 0%, var(--orange-deep) 100%);
    font-family: "Questrial", sans-serif; font-weight: bold; font-size: 13px; color: #fff;
    text-align: center; line-height: 32px; }

  /* Footer */
  .footer { left: 0; top: 713px; width: 1200px; height: 187px; background: var(--footer-bg); }
  .footer-logo-mark { left: 122px; top: 740px; width: 66px; height: 66px; border-radius: 50%;
    background: #3a3a3a; border: 3px solid #5a5a5a; }
  .footer-logo-name { left: 198px; top: 747px; font-family: "Questrial", sans-serif; font-size: 36px; color: #3c3c3c; }
  .footer-nav { left: 372px; top: 752px; font-family: "Questrial", sans-serif; font-size: 13px; color: var(--footer-text); word-spacing: 1px; }
  .footer-nav .sep { margin: 0 17px; }
  .copyright { left: 371px; top: 788px; font-size: 12px; color: var(--footer-text); }
  .social { width: 32px; height: 32px; border-radius: 50%;
    background: radial-gradient(circle at 40% 35%, #bdbdbd 0%, #6d6d6d 100%); }
</style>
</head>
<body>

  <!-- Hero -->
  <div class="abs hero-band"></div>
  <div class="abs hero-shadow"></div>
  <div class="abs hero-photo-left" role="img" aria-label="Photo of a woman lying on a bed texting on a mobile phone"></div>
  <div class="abs hero-photo-right" role="img" aria-label="Photo of a hotel guest in bed using a mobile phone"></div>
  <div class="abs hero-divider"></div>
  <div class="abs hero-caption-bar"></div>
  <svg class="abs hero-badge" viewBox="0 0 112 108" aria-hidden="true">
    <circle cx="56" cy="52" r="54" fill="#f6a623"/>
    <circle cx="56" cy="52" r="44" fill="#1c1c1c"/>
    <circle cx="56" cy="52" r="36" fill="#f39a12"/>
  </svg>
  <p class="abs hero-caption">Keeping in touch with family, friends and work has never been so easy</p>
  <svg class="abs hero-button" viewBox="0 0 172 52" aria-hidden="true">
    <defs>
      <linearGradient id="btnFill" x1="0" y1="0" x2="0" y2="1">
        <stop offset="0" stop-color="#fdb02f"/>
        <stop offset="1" stop-color="#ee7d0c"/>
      </linearGradient>
    </defs>
    <path d="M6 0 H152 L172 26 L152 52 H12 L0 8 Z" fill="url(#btnFill)" stroke="#e07a0a"/>
  </svg>
  <span class="abs hero-button-label">Read More</span>

  <!-- Why choose -->
  <div class="abs section-icon icon-notepad" role="img" aria-label="Illustration of a notepad and magnifying glass"></div>
  <h2 class="abs section-title" style="left:193px;top:235px;">Why Choose US?</h2>
  <div class="abs dotted-rule" style="left:197px;top:263px;width:601px;"></div>
  <ul class="abs reasons">
    <li><svg viewBox="0 0 16 16"><path d="M2 3 L7 3 L11 8 L11 5 L15 5 L15 14 L6 14 L6 10 L9 10 L4 6 Z" fill="#bdbdbd"/></svg>Lorem ipsum dolor sit amet, consectetur adipisicing elit.</li>
    <li><svg viewBox="0 0 16 16"><path d="M2 3 L7 3 L11 8 L11 5 L15 5 L15 14 L6 14 L6 10 L9 10 L4 6 Z" fill="#bdbdbd"/></svg>Sed do eiusmod tempor incididunt ut labore et dolore magna aliqua.</li>
    <li><svg viewBox="0 0 16 16"><path d="M2 3 L7 3 L11 8 L11 5 L15 5 L15 14 L6 14 L6 10 L9 10 L4 6 Z" fill="#bdbdbd"/></svg>Lorem ipsum dolor quis nostrud exercitation ullamco laboris nisi ut aliquip ex</li>
    <li><svg viewBox="0 0 16 16"><path d="M2 3 L7 3 L11 8 L11 5 L15 5 L15 14 L6 14 L6 10 L9 10 L4 6 Z" fill="#bdbdbd"/></svg>Lorem ipsum dolor sit amet, consectetur adipisicing elit</li>
    <li><svg viewBox="0 0 16 16"><path d="M2 3 L7 3 L11 8 L11 5 L15 5 L15 14 L6 14 L6 10 L9 10 L4 6 Z" fill="#bdbdbd"/></svg>Ut enim ad minim veniam, quis nostrud exercitation ullamco laboris nisi ut</li>
  </ul>

  <!-- About -->
  <div class="abs section-icon icon-wallet" role="img" aria-label="Illustration of a leather wallet"></div>
  <h2 class="abs section-title" style="left:191px;top:493px;">About US</h2>
  <div class="abs dotted-rule" style="left:186px;top:517px;width:612px;"></div>
  <p class="abs about-text">Lorem ipsum dolor sit amet, consectetur adipisicing elit, sed do eiusmod tempor incididunt ut labore et dolore magna aliqua. Ut enim ad minim veniam, quis nostrud exercitation ullamco<br>laboris nisi ut aliquip ex ea commodo consequat. Lorem ipsum dolor sit amet, consectetur adipisicing elit, sed do eiusmod tempor incididunt ut labore et dolore magna aliqua. Ut enim ad minim veniam, quis nostrud exercitation ullamco laboris nisi ut aliquip ex ea commodo consequat.</p>
  <a class="abs read-more-link">Read More</a>

  <!-- Testimonial -->
  <div class="abs quote-box"></div>
  <svg class="abs quote-tail" viewBox="0 0 40 22" aria-hidden="true">
    <path d="M0 1 L36 1 L2 21 Z" fill="#e9e9e9"/>
    <path d="M2 21 L36 1" stroke="#dcdcdc" fill="none"/>
    <path d="M2 21 L0 1" stroke="#dcdcdc" fill="none"/>
  </svg>
  <h3 class="abs quote-title">What our clients say</h3>
  <p class="abs quote-text">Lorem ipsum dolor sit amet, con-<br>sectetur adipisicing elit, sed do<br>eiusmod tempor incididunt ut labore<br>et dolore magna aliqua. Ut enim ad<br>minim veniam, quis nostrud exercita-<br>tion ullamco<br>laboris nisi ut aliquip ex ea</p>
  <div class="abs client-photo" role="img" aria-label="Portrait photo of the client"></div>
  <p class="abs client-name">Delia R</p>
  <p class="abs client-role">Hotel Lumen CEO</p>

  <!-- Newsletter -->
  <div class="abs dotted-rule" style="left:817px;top:571px;width:263px;"></div>
  <p class="abs newsletter-title">Join our email list for our newsletter</p>
  <div class="abs newsletter-input">Enter your e-mail</div>
  <div class="abs newsletter-button">SUBSCRIBE</div>

  <!-- Footer -->
  <footer class="abs footer"></footer>
  <div class="abs footer-logo-mark"></div>
  <span class="abs footer-logo-name">ZipRoam</span>
  <nav class="abs footer-nav">FAQs<span class="sep">|</span>Terms Of Use<span class="sep">|</span>Privacy Policy<span class="sep">|</span>Site Map</nav>
  <p class="abs copyright">Copyright © 2012 &nbsp;ZipRoam. All rights reserved.</p>
  <div class="abs social" style="left:952px;top:756px;" aria-label="Social link"></div>
  <div class="abs social" style="left:1001px;top:756px;" aria-label="Social link"></div>

</body>
</html>
```